business card for glass company

logo on business card and letterhead. our business is installing and servicing glass and mirror in commercial and industrial buildings in the Toronto area. full company name, Halvern Glass and Mirror Ltd.
i am looking for a business card and letterhead design.
on the letterhead i need company name and contact info
Halvern Glass and Mirror Ltd.
518 Larchmere Rd.
Toronto, Ontario
M4R 7B9
on the cards the contact info is
Dana Halvern
518 Larchmere Rd.
Toronto, Ontario
M4R 7B9
(416) 555-0142
(416) 555 0187-cell
i need another card with different name
Martin Quell
947 Ash St. N
Hamilton Ontario
L2K 9T3
(416) 555-0142
(416) 555-0163
Target Market(s)
Professionals in industrial and commercial building construction, architects, general contractors, building managers and owners.
Industry/Entity Type
Business
Requirements
Must have
- simple design with two colors. emphasis on the name Halvern.

```html
<!DOCTYPE html>
<html lang="en">
<head>
<meta charset="utf-8">
<title>Halvern Glass and Mirror Ltd. – Stationery</title>
<link href="https://fonts.googleapis.com/css2?family=Roboto:wght@400;700&display=swap" rel="stylesheet">
<style>
  :root {
    --bar-grey: #9c9ea1;
    --board-grey: #c8c9cb;
    --paper: #ffffff;
    --navy: #141f6e;
    --steel: #4a86c8;
    --ink: #1a1a1a;
    --sub-grey: #9a9b9e;
    --edge: #8e8f92;
  }
  * { box-sizing: border-box; margin: 0; padding: 0; }
  html, body { width: 1200px; height: 1200px; overflow: hidden; background: var(--paper); }
  body { position: relative; font-family: "Roboto", Arial, sans-serif; color: var(--ink); }

  .approval-bar {
    position: absolute; left: 0; top: 0; width: 1200px; height: 38px;
    background: var(--bar-grey); color: var(--paper);
    font-size: 19px; letter-spacing: 3px; text-align: center; line-height: 38px;
  }
  .footer-bar {
    position: absolute; left: 0; bottom: 0; width: 1200px; height: 38px;
    background: var(--bar-grey);
  }
  .board {
    position: absolute; left: 15px; top: 54px; width: 1170px; height: 1086px;
    background: var(--board-grey);
  }

  .wordmark {
    font-weight: 700; color: var(--navy); display: flex; align-items: center; justify-content: center;
  }
  .wordmark .mark-square { background: var(--navy); display: inline-block; }
  .tagline { color: var(--sub-grey); text-align: center; letter-spacing: 1px; }
  .gradient-band {
    position: absolute; left: 0; bottom: 0; width: 100%;
    background: linear-gradient(90deg, var(--navy) 0%, var(--navy) 30%, var(--steel) 55%, var(--navy) 80%, #0d1450 100%);
  }

  /* Letterhead */
  .letterhead {
    position: absolute; left: 50px; top: 85px; width: 788px; height: 1024px; background: var(--paper);
  }
  .letterhead .wordmark { position: absolute; top: 28px; left: 0; width: 100%; font-size: 40px; gap: 10px; }
  .letterhead .mark-square { width: 16px; height: 16px; }
  .letterhead .tagline { position: absolute; top: 96px; left: 0; width: 100%; font-size: 15px; }
  .letterhead .contact { position: absolute; left: 0; width: 100%; text-align: center; font-size: 15px; }
  .letterhead .address { top: 925px; }
  .letterhead .phone { top: 960px; }
  .letterhead .gradient-band { height: 19px; }

  /* Large brand lockup */
  .brand-lockup { position: absolute; left: 870px; top: 150px; width: 300px; }
  .brand-lockup .wordmark { font-size: 72px; gap: 14px; }
  .brand-lockup .mark-square { width: 26px; height: 26px; }
  .brand-lockup .tagline { color: var(--paper); font-size: 24px; letter-spacing: 2px; margin-top: 34px; text-align: left; padding-left: 10px; }

  /* Business cards */
  .business-card {
    position: absolute; left: 750px; width: 384px; height: 236px;
    background: var(--paper); border: 1px solid var(--edge);
  }
  .card-dana { top: 416px; }
  .card-martin { top: 708px; }
  .business-card .wordmark { position: absolute; top: 20px; left: 0; width: 100%; font-size: 28px; gap: 8px; }
  .business-card .mark-square { width: 11px; height: 11px; }
  .business-card .tagline { position: absolute; top: 70px; left: 0; width: 100%; font-size: 10px; }
  .business-card .person { position: absolute; top: 112px; left: 0; width: 100%; text-align: center; font-size: 15px; }
  .business-card .details { position: absolute; top: 172px; left: 0; width: 100%; text-align: center; font-size: 11px; line-height: 20px; }
  .business-card .gradient-band { height: 12px; }
</style>
</head>
<body>
  <header class="approval-bar">FOR YOUR APPROVAL</header>

  <main class="board">
  </main>

  <section class="letterhead" aria-label="Letterhead">
    <div class="wordmark"><span>Halvern</span><span class="mark-square"></span></div>
    <div class="tagline">GLASS &amp; MIRROR Ltd</div>
    <p class="contact address">518 Larchmere Road, Toronto, Ontario M4R 7B9</p>
    <p class="contact phone">Phone: (416) 555-0142</p>
    <div class="gradient-band"></div>
  </section>

  <section class="brand-lockup" aria-label="Brand lockup">
    <div class="wordmark"><span>Halvern</span><span class="mark-square"></span></div>
    <div class="tagline">GLASS &amp; MIRROR Ltd</div>
  </section>

  <section class="business-card card-dana" aria-label="Business card, Dana Halvern">
    <div class="wordmark"><span>Halvern</span><span class="mark-square"></span></div>
    <div class="tagline">GLASS &amp; MIRROR Ltd</div>
    <p class="person">Dana Halvern</p>
    <p class="details">518 Larchmere Road, Toronto, Ontario M4R 7B9<br>(416) 555-0142 (416) 555-0187-cell</p>
    <div class="gradient-band"></div>
  </section>

  <section class="business-card card-martin" aria-label="Business card, Martin Quell">
    <div class="wordmark"><span>Halvern</span><span class="mark-square"></span></div>
    <div class="tagline">GLASS &amp; MIRROR Ltd</div>
    <p class="person">Martin Quell</p>
    <p class="details">947 Ash St. N, Hamilton, Ontario L2K 9T3<br>(416) 555-0142 (416) 555-0163</p>
    <div class="gradient-band"></div>
  </section>

  <footer class="footer-bar"></footer>
</body>
</html>
```